Book cover - Rise Above Unease and Bashful Nerves

Book cover for Ebook (Lumora) and wrap around print cover (Printvale) (back, front, and spine)

The book title (may slightly change by end of brief):
(MAIN TITLE) 'Rise Above Unease and Bashful Nerves'
(SUB HEADING) 'A Clear Daily Workbook Guide to Rise Above Unease, Outgrow Timidity and Build Inner Poise'
by Dr Owen Farrby

I would like a bold, stand out cover. Contemporary. I would like to avoid stereotypical images of people looking anxious or worried. I would like the design to be more uplifting and hopeful, rather than focusing on the negative aspect of anxiety, but avoiding cliched photos of people raising their hands in the air, smiling and jumping etc. The cover should appeal to both men and women.

Trim size of book cover (for PrintVale) is 5.25" x 8" back and front with a spine size of 0.477 inches

Reason: I have decided to extend the deadline by 1 more day, not because I am unhappy with the quality of the designs, but because a few designers have contacted me to explain they have had technical difficulties when submitting their files. Thanks everyone for the hard work and great designs.

Target Market(s)

Males and females (16+) who struggle with social anxiety and shyness

Industry/Entity Type

Social

Font styles to use
Serif

Requirements
Must have
• Bold cover that is modern and contemporary. For example, I like these covers:
• http://qvlk.io/8kTz3Pm
• http://qvlk.io/9wHe5Nb
• http://qvlk.io/4jMr7Yc
• http://qvlk.io/6nGs2Lq
• http://qvlk.io/3fVb81t
• http://qvlk.io/7yKd4Ue
• http://qvlk.io/5hWx9Oa
Nice to have
• Open to abstract designs.
Should not have
• No stereotypical pictures of people who look anxious or worried. Avoid cliched photos of people raising their hands in the air, smiling and jumping etc.

```html
<!DOCTYPE html>
<html lang="en">
<head>
<meta charset="UTF-8">
<title>Rise Above Unease and Bashful Nerves — Dr Owen Farrby</title>
<link rel="stylesheet" href="https://fonts.googleapis.com/css2?family=Bebas+Neue&family=Arimo:wght@400&display=swap">
<style>
  :root {
    --paper: #ffffff;
    --paper-shade: #eeeeee;
    --title-light: #2cb4e8;
    --title-dark: #1463ae;
    --ink: #2b2b2b;
    --spinner-main: #2ab8dc;
    --spinner-soft: #dff2f8;
    --ring-grey: #e2e2e2;
  }
  html, body {
    margin: 0;
    padding: 0;
    width: 787px;
    height: 1200px;
    overflow: hidden;
    background: var(--paper);
  }
  .cover {
    position: relative;
    width: 787px;
    height: 1200px;
    overflow: hidden;
    background:
      radial-gradient(ellipse at 15% 10%, var(--paper-shade) 0%, transparent 45%),
      radial-gradient(ellipse at 90% 40%, var(--paper-shade) 0%, transparent 40%),
      radial-gradient(ellipse at 20% 85%, var(--paper-shade) 0%, transparent 40%),
      var(--paper);
  }
  .title {
    position: absolute;
    top: 4px;
    left: 0;
    width: 100%;
    margin: 0;
    text-align: center;
    font-family: "Bebas Neue", "Oswald", sans-serif;
    font-weight: 400;
    line-height: 0.86;
  }
  .title-line {
    display: block;
    font-size: 114px;
    letter-spacing: 2px;
    background: linear-gradient(180deg, var(--title-light) 10%, var(--title-dark) 90%);
    -webkit-background-clip: text;
    background-clip: text;
    color: transparent;
  }
  .title-line--joined {
    display: flex;
    justify-content: center;
    align-items: center;
    gap: 6px;
  }
  .title-and {
    display: inline-block;
    writing-mode: vertical-rl;
    transform: rotate(180deg);
    font-size: 34px;
    letter-spacing: 1px;
    line-height: 1;
    color: var(--title-dark);
  }
  .title-words {
    font-size: 104px;
    background: linear-gradient(180deg, var(--title-light) 10%, var(--title-dark) 90%);
    -webkit-background-clip: text;
    background-clip: text;
    color: transparent;
  }
  .subtitle {
    position: absolute;
    top: 322px;
    left: 110px;
    width: 567px;
    margin: 0;
    text-align: center;
    font-family: "Arimo", Arial, sans-serif;
    font-size: 25px;
    line-height: 1.24;
    color: var(--ink);
  }
  .artwork {
    position: absolute;
    top: 470px;
    left: 30px;
    width: 727px;
    height: 540px;
  }
  .author {
    position: absolute;
    bottom: 22px;
    left: 0;
    width: 100%;
    margin: 0;
    text-align: center;
    font-family: "Bebas Neue", "Oswald", sans-serif;
    font-weight: 400;
    font-size: 70px;
    letter-spacing: 2px;
    background: linear-gradient(180deg, var(--title-light) 10%, var(--title-dark) 90%);
    -webkit-background-clip: text;
    background-clip: text;
    color: transparent;
  }
</style>
</head>
<body>
<main class="cover">
  <h1 class="title">
    <span class="title-line">Rise Above</span>
    <span class="title-line">Unease</span>
    <span class="title-line title-line--joined">
      <span class="title-and">and</span>
      <span class="title-words">Bashful Nerves</span>
    </span>
  </h1>

  <p class="subtitle">A Clear Daily Workbook Guide to Rise Above Unease, Outgrow Timidity and Build Inner Poise</p>

  <svg class="artwork" viewBox="0 0 727 540" role="img" aria-label="Blue fidget spinner spinning over a faint ring of words about worry and stress">
    <defs>
      <radialGradient id="ring-fade" cx="50%" cy="50%" r="50%">
        <stop offset="0%" stop-color="#ffffff"/>
        <stop offset="55%" stop-color="#f4f4f4"/>
        <stop offset="80%" stop-color="var(--ring-grey)"/>
        <stop offset="100%" stop-color="#ffffff" stop-opacity="0"/>
      </radialGradient>
      <radialGradient id="spinner-glow" cx="50%" cy="48%" r="50%">
        <stop offset="0%" stop-color="var(--spinner-main)"/>
        <stop offset="60%" stop-color="var(--spinner-main)" stop-opacity="0.75"/>
        <stop offset="100%" stop-color="var(--spinner-soft)" stop-opacity="0"/>
      </radialGradient>
    </defs>
    <ellipse cx="363" cy="270" rx="355" ry="265" fill="url(#ring-fade)"/>
    <ellipse cx="365" cy="260" rx="300" ry="210" fill="url(#spinner-glow)"/>
  </svg>

  <p class="author">Dr Owen Farrby</p>
</main>
</body>
</html>
```